Package Design for Plant-based Dumplings

We need a CPG Package design for a new product we're launching. I included example (front and back) of what a typical information food package has, so you can use it as reference.

Target Market(s)

Consumers that are seeking non-meat items. Environment concerned consumers.

Colors

Designer to choose colors to be used in the design.

Requirements
Must have
• Modern and clean looking design.
Nice to have
• might have multiple flavors, so make design where it could be have multiple variations.

```html
<!DOCTYPE html>
<html lang="en">
<head>
<meta charset="utf-8">
<title>MaeRin Foods – Plant-Based Dumplings Package</title>
<link href="https://fonts.googleapis.com/css2?family=Arimo:wght@400;700&family=Open+Sans:wght@600;700&display=swap" rel="stylesheet">
<style>
  :root {
    --brand-orange: #f64a14;
    --ink: #111111;
    --paper: #ffffff;
    --slate-dark: #2a2b2d;
    --rule: #222222;
  }
  * { box-sizing: border-box; margin: 0; padding: 0; }
  html, body { width: 1200px; height: 912px; overflow: hidden; background: var(--paper); }
  body { position: relative; font-family: "Arimo", Arial, sans-serif; color: var(--ink); }

  /* ---------- Front panel ---------- */
  .front-panel {
    position: absolute; left: 43px; top: 67px; width: 551px; height: 771px;
    border: 1px solid #555; overflow: hidden; background: var(--paper);
  }
  .product-photo {
    position: absolute; left: 0; top: 0; width: 100%; height: 734px;
    background: radial-gradient(ellipse at 48% 62%, #6b6a5c 0%, #3b3c3e 38%, var(--slate-dark) 70%, #1f2022 100%);
  }
  .top-band { position: absolute; left: 0; top: 0; width: 551px; height: 220px; }
  .front-brand {
    position: absolute; left: 112px; top: 48px;
    display: flex; align-items: center; gap: 14px;
  }
  .brand-name {
    font-family: "Arimo", Arial, sans-serif; font-weight: 700; color: var(--ink);
    line-height: 0.95;
  }
  .front-brand .brand-name { font-size: 44px; }
  .brand-dot { border-radius: 50%; background: var(--brand-orange); flex: none; }
  .front-brand .brand-dot { width: 110px; height: 110px; border: 3px solid var(--paper); }

  .title-plate {
    position: absolute; left: 0; top: 184px; width: 427px; height: 77px;
    background: var(--brand-orange); border-radius: 0 10px 10px 0;
    color: var(--paper); font-family: "Open Sans", Arial, sans-serif; padding-left: 26px;
  }
  .title-plate h1 { font-size: 33px; font-weight: 700; line-height: 1; margin-top: 8px; letter-spacing: 0.2px; }
  .title-plate p { font-size: 19px; font-weight: 600; margin-top: 5px; padding-left: 5px; }

  .claim-badges { position: absolute; left: 228px; top: 645px; display: flex; gap: 10px; }
  .claim-badge { position: relative; width: 72px; height: 77px; }
  .claim-badge svg { position: absolute; inset: 0; }
  .claim-badge span {
    position: absolute; inset: 0; display: flex; align-items: center; justify-content: center;
    text-align: center; color: var(--paper); font-family: "Open Sans", Arial, sans-serif;
    font-weight: 600; font-size: 15px; line-height: 1;
  }

  .front-footer {
    position: absolute; left: 0; bottom: 0; width: 100%; height: 37px;
    display: flex; justify-content: space-between; align-items: center; padding: 0 10px 0 9px;
    color: var(--brand-orange); font-family: "Open Sans", Arial, sans-serif; font-weight: 600; font-size: 21px;
  }

  /* ---------- Back panel ---------- */
  .back-panel {
    position: absolute; left: 607px; top: 69px; width: 549px; height: 769px;
    border: 1px solid #555; background: var(--paper);
  }
  .back-brand {
    position: absolute; left: 82px; top: 24px; display: flex; align-items: center; gap: 16px;
  }
  .back-brand .brand-name { font-size: 46px; }
  .back-brand .brand-dot { width: 110px; height: 110px; }

  .brand-story {
    position: absolute; left: 21px; top: 150px; width: 520px;
    font-size: 14.6px; font-weight: 700; line-height: 22.9px;
  }
  .ingredients {
    position: absolute; left: 21px; top: 322px; width: 330px;
    font-size: 6.6px; font-weight: 700; line-height: 15px; text-transform: uppercase;
  }
  .ingredients .gap { display: block; height: 15px; }
  .allergens { position: absolute; left: 21px; top: 537px; font-size: 7px; font-weight: 700; }
  .heating {
    position: absolute; left: 21px; top: 567px; width: 360px;
    font-size: 7px; font-weight: 700; line-height: 15px;
  }

  .nutrition-facts {
    position: absolute; left: 358px; top: 315px; width: 157px; height: 282px;
    border: 1px solid var(--rule); padding: 3px 5px; font-size: 6.6px; line-height: 1.15;
  }
  .nutrition-facts h2 { font-size: 17px; font-weight: 700; line-height: 1; }
  .nf-row { display: flex; justify-content: space-between; border-top: 0.6px solid #888; padding: 2px 0 1.6px; }
  .nf-row b { font-weight: 700; }
  .nf-thick { border-top: 5px solid var(--rule); }
  .nf-mid { border-top: 2.5px solid var(--rule); }
  .nf-calories { display: flex; justify-content: space-between; align-items: flex-end; font-weight: 700; }
  .nf-calories .label { font-size: 13px; }
  .nf-calories .value { font-size: 19px; line-height: 1; }
  .nf-note { font-size: 4.6px; line-height: 1.3; border-top: 3px solid var(--rule); padding-top: 2px; margin-top: 1px; }

  .barcode-label { position: absolute; left: 414px; top: 613px; font-size: 11.5px; font-weight: 700; }
  .barcode-box {
    position: absolute; left: 376px; top: 626px; width: 139px; height: 72px;
    border: 1px solid var(--rule); display: flex; align-items: center; justify-content: center;
    font-size: 11.5px; font-weight: 700;
  }
  .manufacturer {
    position: absolute; right: 33px; top: 716px; text-align: right;
    font-size: 6.6px; font-weight: 700; line-height: 15px;
  }
</style>
</head>
<body>

<section class="front-panel">
  <div class="product-photo" role="img" aria-label="Overhead photo of pan-fried plant-based dumplings with sesame seeds in a cast-iron skillet on a dark slate surface, with wooden chopsticks"></div>

  <svg class="top-band" viewBox="0 0 551 220" aria-hidden="true">
    <path d="M0 0 H551 V170 C470 205 390 200 320 172 C250 145 150 135 60 150 C30 155 10 165 0 175 Z" fill="var(--paper)"/>
    <path d="M30 0 H551 V120 C500 150 430 160 360 140 C300 120 230 100 150 110 C90 118 40 140 0 165 V60 Z" fill="var(--brand-orange)"/>
  </svg>

  <div class="front-brand">
    <span class="brand-name">MaeRin<br>Foods</span>
    <span class="brand-dot"></span>
  </div>

  <div class="title-plate">
    <h1>Plant-Based Dumplings</h1>
    <p>Using Plant-based Meat and Vegetables</p>
  </div>

  <div class="claim-badges">
    <div class="claim-badge">
      <svg viewBox="0 0 72 77"><polygon points="36,2 69,20.5 69,56.5 36,75 3,56.5 3,20.5" fill="var(--brand-orange)" stroke="var(--paper)" stroke-width="2" stroke-linejoin="round"/></svg>
      <span>Vegan</span>
    </div>
    <div class="claim-badge">
      <svg viewBox="0 0 72 77"><polygon points="36,2 69,20.5 69,56.5 36,75 3,56.5 3,20.5" fill="var(--brand-orange)" stroke="var(--paper)" stroke-width="2" stroke-linejoin="round"/></svg>
      <span>Ready in<br>Minutes</span>
    </div>
    <div class="claim-badge">
      <svg viewBox="0 0 72 77"><polygon points="36,2 69,20.5 69,56.5 36,75 3,56.5 3,20.5" fill="var(--brand-orange)" stroke="var(--paper)" stroke-width="2" stroke-linejoin="round"/></svg>
      <span>No Soy</span>
    </div>
    <div class="claim-badge">
      <svg viewBox="0 0 72 77"><polygon points="36,2 69,20.5 69,56.5 36,75 3,56.5 3,20.5" fill="var(--brand-orange)" stroke="var(--paper)" stroke-width="2" stroke-linejoin="round"/></svg>
      <span>20g of<br>Protein</span>
    </div>
  </div>

  <footer class="front-footer">
    <span>Net Wt. 2 LBs (32oz)</span>
    <span>Keep Frozen</span>
  </footer>
</section>

<section class="back-panel">
  <div class="back-brand">
    <span class="brand-name">MaeRin<br>Foods</span>
    <span class="brand-dot"></span>
  </div>

  <p class="brand-story">The brand name MaeRin Foods was inspired from a lady named Mae Rin that started a food business in S. Korea during the 1950s. Mae’s family immigrated to the U.S. in late 1990s and the Rin family began making dumplings out-of-their home kitchen and sold into local markets.&nbsp; Business grew and the family eventually built a state-of-the-art USDA food factory in 2003.&nbsp; Dumplings made at MaeRin’s factory is now available throughout retailers in US and Canada.</p>

  <div class="ingredients">
    Ingredient list<br>
    Filling:&nbsp; Plant-based meat(water, pea protein isolate,canola and sunflower oil, rice flour, spice, tomato powder,contains 0.5% or less: yeast extract, sugar, potassium chloride,tapioca maltodextrin, citric acid, salt, acacia gum, onion extract,natural flavor, garlic extract ), cabbage, onion, sweet potato noodle(water, sweet potato starch), green onion, seasoning(onion powder, grilled flavor, sugar, garlic dehydrated, spice,natural flavor, yeast extract), carrot, water, starch (cornstarch,modified starch), sesame oil,&nbsp; canola oil, garlic.
    <span class="gap"></span>
    Dough:wheat flour enriched([niacin, reduced iron, thiamine mononitrate, riboflavin, folic acid] malted barley flour),water, conditioner(tapioca starch, salt, dextrose, potassium chloride, monoglycerides, modified cellulose gum, xanthan gum),canola oil.
  </div>

  <p class="allergens">Allergens: Wheat</p>

  <div class="heating">
    Heating Instructions<br>
    Steam:<br>
    1. Remove frozen dumplings from the package and place them in a steamer over boiling water.<br>
    2. Cover the steamer approximately 8-10 minutes or until cooked thoroughly.<br>
    Pan Fry:<br>
    1. Heat 2 teaspoons of oil in frying pan. Carefully place thawed dumplings into heated pan.<br>
    2. Heat approximately 3-4 minutes or until golden brown.<br>
    Microwave:<br>
    1. Place frozen dumplings on microwave-safe dish.<br>
    2. Cover with damp paper towel and heat on high for 2 to 3 minutes or until hot.
  </div>

  <div class="nutrition-facts">
    <h2>Nutrition Facts</h2>
    <div style="font-size:7.4px;border-top:0.6px solid #888;margin-top:2px;padding-top:1px">about 8 servings per container</div>
    <div class="nf-calories" style="font-size:8px"><span>Servings Size</span><span>3 pieces (90g)</span></div>
    <div class="nf-thick" style="margin-top:2px;padding-top:2px;font-size:5px;font-weight:700">Amount per serving</div>
    <div class="nf-calories"><span class="label">Calories</span><span class="value">180</span></div>
    <div class="nf-row nf-mid" style="justify-content:flex-end;font-size:5.4px"><b>% Daily Value</b></div>
    <div class="nf-row"><span><b>Total Fat</b> 8g</span><b>10%</b></div>
    <div class="nf-row"><span>Saturdated Fat 2.5g</span><b>13%</b></div>
    <div class="nf-row"><span>Trans&nbsp;&nbsp;&nbsp; Fat 0g</span><span></span></div>
    <div class="nf-row"><span><b>Cholesterol</b> 15mg</span><b>5%</b></div>
    <div class="nf-row"><span><b>Sodium</b> 410mg</span><b>18%</b></div>
    <div class="nf-row"><span><b>Total Carbohydrate</b> 19g</span><b>7%</b></div>
    <div class="nf-row"><span>Dietary Fiber 1g</span><b>4%</b></div>
    <div class="nf-row"><span>Total Sugars 2g</span><span></span></div>
    <div class="nf-row"><span>Includes 1g Added Sugars</span><b>2%</b></div>
    <div class="nf-row"><span><b>Protein</b> 8g</span><span></span></div>
    <div class="nf-row nf-thick"><span>Vitamin D&nbsp; 0mcg</span><span>0%</span></div>
    <div class="nf-row"><span>Calcium 30mg</span><span>2%</span></div>
    <div class="nf-row"><span>Iron 1.2mg</span><span>6%</span></div>
    <div class="nf-row"><span>Potassium 176mg</span><span>4%</span></div>
    <p class="nf-note">* The % Daily Value tells you how much a nutrient in a serving of food contributes to a daily diet.&nbsp; 2000 calories a day is used for general nutrition advice.</p>
  </div>

  <p class="barcode-label">Barcode:</p>
  <div class="barcode-box">place-holder for now</div>

  <div class="manufacturer">
    Manufactured For:<br>
    Northfield Company<br>
    Fresno, CA 93650
  </div>
</section>

</body>
</html>
```